Hadley & Partners, LLC Business Card 2016

We need a new business card design for a very important trade show coming up.

We are a compliance Consulting Firm. Our clients are stock brokerage firms and investment advisers.

I would like our logo on both sides of the card.

Info in the front of the card shold include:

Logo
First & Last Name
Title
Office #
Cell #
Email
Company Address (42 W. Calloway St., Suite 300 Pasadena, CA 91417

Back of the card should include the logo and url: www.hadleypartnersgroup.com

Target Market(s)

Stock Brokerage Firms and Investment Advisers

Industry/Entity Type

Financial Service

Contact Information for Business Card

Marcus J. Pellew
President
42 W. Calloway St., Suite 300
Pasadena, CA 91417
O 626.555.0147 ext. 204
C 818.555.0193
Email: marcus@hadleypartnersgroup.com
www.hadleypartnersgroup.com

Requirements
Nice to have
• The back of the card could be black with the logo with the white letters.
• I do want the front of the card to at least have the color logo with the black "Hadley & Partners Lettering.

```html
<!DOCTYPE html>
<html lang="en">
<head>
<meta charset="utf-8">
<title>Hadley &amp; Partners — Business Card</title>
<link href="https://fonts.googleapis.com/css2?family=Open+Sans:wght@400;600;700&display=swap" rel="stylesheet">
<style>
  :root {
    --page: #e9e6e3;
    --card: #1f2a35;
    --ink: #ffffff;
    --ink-soft: #c9d0d6;
    --accent: #e8343a;
    --shadow: rgba(0, 0, 0, 0.28);
  }
  * { margin: 0; padding: 0; box-sizing: border-box; }
  html, body {
    width: 1200px;
    height: 900px;
    overflow: hidden;
    background: var(--page);
    font-family: "Open Sans", Arial, sans-serif;
    color: var(--ink);
  }
  .canvas { position: relative; width: 1200px; height: 900px; }
  .card {
    position: absolute;
    width: 556px;
    height: 342px;
    background: var(--card);
    box-shadow: 0 10px 24px var(--shadow);
  }
  .card--front { left: 238px; top: 62px; }
  .card--back { left: 457px; top: 518px; width: 560px; }

  /* front */
  .brand-mark {
    position: absolute;
    left: 26px;
    top: 96px;
    width: 210px;
    display: flex;
    flex-direction: column;
    align-items: center;
    gap: 14px;
  }
  .brand-mark__square {
    width: 56px;
    height: 56px;
    background: var(--accent);
  }
  .brand-mark__name {
    font-weight: 700;
    font-size: 18px;
    letter-spacing: 0.2px;
    white-space: nowrap;
  }
  .contact {
    position: absolute;
    left: 262px;
    top: 76px;
  }
  .contact__name { font-size: 18px; font-weight: 700; line-height: 24px; }
  .contact__title { font-size: 15px; line-height: 20px; }
  .contact__address { margin-top: 13px; font-size: 15px; line-height: 20px; }
  .contact__list { list-style: none; margin-top: 14px; }
  .contact__item {
    display: flex;
    align-items: center;
    font-size: 15px;
    line-height: 20px;
  }
  .contact__icon {
    width: 12px;
    height: 12px;
    margin-right: 8px;
    flex: none;
    fill: var(--ink);
  }

  /* back */
  .back-brand {
    position: absolute;
    left: 0;
    right: 0;
    top: 92px;
    display: flex;
    flex-direction: column;
    align-items: center;
  }
  .back-brand__square {
    width: 80px;
    height: 80px;
    background: var(--accent);
  }
  .back-brand__name {
    margin-top: 20px;
    font-weight: 700;
    font-size: 32px;
    line-height: 40px;
    letter-spacing: 0.5px;
  }
  .back-brand__url {
    margin-top: 10px;
    font-size: 14px;
    line-height: 18px;
    letter-spacing: 0.6px;
    color: var(--ink-soft);
  }
</style>
</head>
<body>
<main class="canvas">

  <section class="card card--front" aria-label="Card front">
    <div class="brand-mark">
      <span class="brand-mark__square"></span>
      <span class="brand-mark__name">Hadley &amp; Partners</span>
    </div>

    <div class="contact">
      <p class="contact__name">Marcus J. Pellew</p>
      <p class="contact__title">President</p>
      <p class="contact__address">42 W. Calloway St., Suite 300<br>Pasadena, CA 91417</p>
      <ul class="contact__list">
        <li class="contact__item">
          <svg class="contact__icon" viewBox="0 0 12 12" aria-hidden="true"><path d="M2.4 0.6 L4.2 2.6 L3.2 4 C3.9 5.6 5.4 7.2 7.8 8.6 L9.2 7.6 L11.4 9.4 L10.4 11.4 C5.2 11.2 0.8 6.8 0.6 1.6 Z"/></svg>
          626.555.0147 ext. 204
        </li>
        <li class="contact__item">
          <svg class="contact__icon" viewBox="0 0 12 12" aria-hidden="true"><path d="M3 0 H9 V12 H3 Z M4 1.2 V9.6 H8 V1.2 Z M5.4 10.2 H6.6 V11.2 H5.4 Z"/></svg>
          818.555.0193
        </li>
        <li class="contact__item">
          <svg class="contact__icon" viewBox="0 0 12 12" aria-hidden="true"><path d="M1 3 H11 V10 H1 Z M1.6 3.4 L6 6.6 L10.4 3.4" stroke="#1f2a35" stroke-width="0.8"/></svg>
          marcus@hadleypartnersgroup.com
        </li>
        <li class="contact__item">
          <svg class="contact__icon" viewBox="0 0 12 12" aria-hidden="true"><circle cx="6" cy="6" r="5.4"/><path d="M3 4 C4.5 3 5 5 6.5 4.5 M5 8.5 C6 7.5 7.5 9 8.5 7.5" stroke="#1f2a35" stroke-width="1" fill="none"/></svg>
          www.hadleypartnersgroup.com
        </li>
      </ul>
    </div>
  </section>

  <section class="card card--back" aria-label="Card back">
    <div class="back-brand">
      <span class="back-brand__square"></span>
      <span class="back-brand__name">Hadley &amp; Partners</span>
      <span class="back-brand__url">www.hadleypartnersgroup.com</span>
    </div>
  </section>

</main>
</body>
</html>
```